Packaging Design job - Natural Sleep Aid Supplement

We need a packaging design theme for a Natural Sleep Aid Supplement allowing a fall asleep fast and a good quality of sleep. This product will be in blister form of 15 capsules. We need for this a packaging design for the box.Dimensions: 75 * 25 * 116 mmThe active ingredients are: passionflower; lemon balm and valerianProduct Name: SOMNATWe would like to see clean, modern and fresh designs.This should give the impression of professional products of pharmaceutical quality.You will also find attached the logo of our company.Ps : You can change the color of the logo

Font styles to use
Serif
Sans Serif

Colors

Designer to choose colors to be used in the design.

Requirements
Should not have
• Sales and other "must buy" "guaranteed" etc

```html
<!DOCTYPE html>
<html lang="en">
<head>
<meta charset="utf-8">
<title>Dorvelia – Natural Sleep Aid Supplement</title>
<link href="https://fonts.googleapis.com/css2?family=Questrial&family=Oswald:wght@400&family=Noticia+Text&display=swap" rel="stylesheet">
<style>
  :root {
    --page: #ffffff;
    --petal-light: #f4f4f5;
    --petal-mid: #dedfe3;
    --flower-blue: #3c4f8f;
    --flower-violet: #3a2550;
    --flower-deep: #1e1530;
    --pollen: #e0a12a;
    --brand-teal: #1fb5b0;
    --title-brown: #3a1e12;
    --ink: #1c1c1c;
    --ingredient-navy: #2a3560;
  }
  * { margin: 0; padding: 0; box-sizing: border-box; }
  html, body {
    width: 1200px;
    height: 700px;
    overflow: hidden;
    background: var(--page);
  }
  .box-front {
    position: absolute;
    left: 100px;
    top: 28px;
    width: 1000px;
    height: 644px;
    overflow: hidden;
  }
  .flower-photo {
    position: absolute;
    inset: 0;
    background:
      radial-gradient(ellipse 6% 8% at 70% 58%, var(--flower-blue) 0%, transparent 100%),
      radial-gradient(ellipse 22% 30% at 67% 68%, var(--flower-blue) 0%, var(--flower-violet) 55%, transparent 100%),
      radial-gradient(ellipse 32% 44% at 67% 70%, rgba(224,161,42,0.55) 0%, rgba(58,37,80,0.6) 55%, transparent 78%),
      radial-gradient(ellipse 70% 90% at 66% 72%, var(--petal-mid) 0%, var(--petal-light) 70%);
  }
  .brand {
    position: absolute;
    left: 50px;
    top: 84px;
    display: flex;
    align-items: center;
    gap: 12px;
    font-family: "Questrial", sans-serif;
    font-size: 38px;
    letter-spacing: 1px;
    color: var(--brand-teal);
  }
  .brand-dot {
    width: 18px;
    height: 18px;
    border-radius: 50%;
    background: var(--brand-teal);
  }
  .capsule-count {
    position: absolute;
    left: 842px;
    top: 16px;
    font-family: "Oswald", sans-serif;
    font-size: 31px;
    line-height: 1.35;
    color: var(--ink);
  }
  .product-name {
    position: absolute;
    left: 64px;
    top: 206px;
    font-family: "Questrial", sans-serif;
    font-size: 70px;
    letter-spacing: 2px;
    color: var(--title-brown);
    line-height: 1;
  }
  .product-type {
    position: absolute;
    left: 65px;
    top: 288px;
    font-family: "Questrial", sans-serif;
    font-size: 17px;
    letter-spacing: 0.6px;
    color: var(--ink);
  }
  .ingredients {
    position: absolute;
    left: 29px;
    top: 538px;
    font-family: "Noticia Text", serif;
    font-size: 21px;
    line-height: 1.3;
    color: var(--ingredient-navy);
  }
</style>
</head>
<body>
  <main class="box-front">
    <div class="flower-photo" role="img" aria-label="Close-up photograph of a white daisy-like flower with a blue and violet centre dotted with orange pollen"></div>
    <div class="brand"><span class="brand-dot"></span>NOCTIVA</div>
    <div class="capsule-count">15<br>CAPSULES</div>
    <h1 class="product-name">DORVELIA</h1>
    <p class="product-type">NATURAL SLEEP AID SUPPLEMENT</p>
    <p class="ingredients">Made with passion flower,<br>lemon balm and valerian</p>
  </main>
</body>
</html>
```